ZentaLOOM new era @ Hyper Digitalization

We need a Brochure that show all our product, services and consulting related to Hyper Digitalization into the industrial internet of things world.
We need a document that can be handled as a electronic brochure, this means that we need to show strong corporate presence, with strong skill of technology, and we have credentials and key sucess projects related to Manufacturing industries.
Key industries that we attend: Automotive, Chemical, Food and Beverage, Mining, Paper and Pulp, Oil and Gas, Energy Management.
We save money to our customer in 6 ways: 1) Eficiency in operation 2) Production Control 3) Hyper Digitalization of Thing Optimizing asset ussage 4) Maintenance and predictive of assets risks 5) Quality Control reducing Cost 6) Augmented Reality in operation and control
Target Market(s)
Manufacturing Industry. CEO of companies that has challenges of saving operation costs into plants of manufacturing.
Industry/Entity Type
Software
Font styles to use
Other font styles liked:
- MONTSERRAT
Requirements
Must have
- Technology Enviroment, our logo, our expertise, simple message about what our company does and the DNA, infography of the company, cases of sucess, cases of savings $ using our tecnology and services, what we can do for the customer in a few words
Nice to have
- standarize our colors related to our presentation, futuristic, information related to Artificial Inteligence related to machinery
Should not have
- old version of technology,

```html
<!DOCTYPE html>
<html lang="en">
<head>
<meta charset="utf-8">
<title>ZentaLOOM Brochure 2021 – Cover Spread</title>
<link rel="stylesheet" href="https://fonts.googleapis.com/css2?family=Montserrat:wght@300;400;500;800&family=Lato:wght@400&display=swap">
<style>
  :root {
    --backdrop: #2a2a2a;
    --backdrop-light: #383838;
    --navy: #31495f;
    --navy-deep: #27394f;
    --band: #3b5a78;
    --space-dark: #0c1630;
    --space-mid: #26457c;
    --space-glow: #9ab8e6;
    --paper: #eef1f8;
    --white: #ffffff;
    --text-soft: #c9d3de;
    --brand-ink: #31495f;
    --rule: #8a9bb0;
  }
  * { box-sizing: border-box; margin: 0; padding: 0; }
  html, body { width: 1200px; height: 789px; overflow: hidden; }
  body {
    background: radial-gradient(ellipse at center, var(--backdrop-light) 0%, var(--backdrop) 75%);
    font-family: "Montserrat", sans-serif;
    position: relative;
  }
  .spread {
    position: absolute;
    left: 180px; top: 97px;
    width: 840px; height: 594px;
    display: flex;
    box-shadow: 0 20px 50px rgba(0,0,0,.55);
  }
  .page { position: relative; width: 420px; height: 594px; overflow: hidden; }

  /* Back cover */
  .back-cover {
    background: linear-gradient(165deg, var(--navy) 0%, var(--navy-deep) 100%);
    color: var(--white);
  }
  .back-cover::after {
    content: ""; position: absolute; top: 0; right: 0; width: 30px; height: 100%;
    background: linear-gradient(90deg, rgba(0,0,0,0) 0%, rgba(0,0,0,.14) 100%);
  }
  .about-text {
    position: absolute; left: 44px; top: 236px; width: 332px;
    font-size: 9.6px; line-height: 1.42; font-weight: 500; color: var(--white);
    text-align: justify;
  }
  .brand-name {
    font-family: "Montserrat", sans-serif; font-weight: 400; letter-spacing: .5px;
  }
  .back-cover .brand-name {
    position: absolute; left: 0; right: 0; top: 430px; text-align: center;
    font-size: 21px; color: var(--white);
  }
  .contact-row {
    position: absolute; left: 30px; right: 30px; top: 506px;
    display: flex; justify-content: space-between; align-items: center;
    font-family: "Lato", sans-serif; font-style: normal;
    font-size: 8.5px; line-height: 1.3; color: var(--text-soft);
  }
  .contact-item { display: flex; align-items: center; gap: 8px; }
  .contact-item + .contact-item { border-left: 1px solid var(--rule); padding-left: 12px; }
  .contact-icon { width: 14px; height: 14px; flex: none; }

  /* Front cover */
  .front-cover { background: var(--navy); }
  .front-cover::before {
    content: ""; position: absolute; top: 0; left: 0; width: 30px; height: 100%; z-index: 2;
    background: linear-gradient(90deg, rgba(0,0,0,.16) 0%, rgba(0,0,0,0) 100%);
  }
  .cover-art { position: absolute; inset: 0; }
  .cover-title {
    position: absolute; left: 96px; top: 290px; color: var(--white);
  }
  .cover-title h1 { font-size: 30px; font-weight: 800; letter-spacing: .5px; line-height: 1; }
  .cover-title p { font-size: 17px; font-weight: 300; margin-top: 6px; }
  .front-cover .brand-name {
    position: absolute; right: 34px; top: 468px; font-size: 21px; color: var(--brand-ink);
  }
</style>
</head>
<body>
  <main class="spread">
    <section class="page back-cover">
      <p class="about-text">ZentaLOOM brings hyper digitalization to the industrial internet of things. Our software, services and consulting connect every machine, line and plant, so leaders see their operation in real time and act before costs appear. We serve automotive, chemical, food and beverage, mining, paper and pulp, oil and gas and energy management. Our clients save money in six ways: efficiency in operation, production control, digitalized things that optimize asset usage, predictive maintenance of asset risks, quality control that reduces cost, and augmented reality in operation and control. Artificial intelligence learns from your machinery and turns data into decisions. Proven cases across manufacturing show measurable savings within the first year. A new era starts with ZentaLOOM.</p>

      <div class="brand-name">ZentaLOOM</div>

      <address class="contact-row">
        <div class="contact-item">
          <svg class="contact-icon" viewBox="0 0 14 14" aria-hidden="true"><path d="M7 1a4 4 0 0 0-4 4c0 3 4 8 4 8s4-5 4-8a4 4 0 0 0-4-4zm0 5.6A1.6 1.6 0 1 1 7 3.4a1.6 1.6 0 0 1 0 3.2z" fill="#c9d3de"/></svg>
          <span>48 Foundry Lane,<br>Brookvale, USA 10482</span>
        </div>
        <div class="contact-item">
          <svg class="contact-icon" viewBox="0 0 14 14" aria-hidden="true"><path d="M3.2 1.5l2 2.3-1 1.4a7 7 0 0 0 4.6 4.6l1.4-1 2.3 2-1.1 1.7C6.5 12.3 1.7 7.5 1.5 2.6z" fill="#c9d3de"/></svg>
          <span>+000 555 210 340<br>+000 555 210 340</span>
        </div>
        <div class="contact-item">
          <svg class="contact-icon" viewBox="0 0 14 14" aria-hidden="true"><circle cx="7" cy="7" r="6" fill="#c9d3de"/><path d="M1.5 7h11M7 1.2c-2 2.2-2 9.4 0 11.6M7 1.2c2 2.2 2 9.4 0 11.6" stroke="#31495f" stroke-width=".8" fill="none"/></svg>
          <span>hello@zentaloom.com<br>www.zentaloom.com</span>
        </div>
      </address>
    </section>

    <section class="page front-cover">
      <svg class="cover-art" viewBox="0 0 420 594" width="420" height="594">
        <defs>
          <radialGradient id="space-fill" cx="0.72" cy="0.42" r="0.65">
            <stop offset="0" stop-color="#9ab8e6"/>
            <stop offset="0.28" stop-color="#26457c"/>
            <stop offset="1" stop-color="#0c1630"/>
          </radialGradient>
        </defs>
        <polygon points="40,0 420,0 420,272" fill="url(#space-fill)" role="img" aria-label="Photograph of Earth from orbit at night, with glowing network lines across the globe"/>
        <polygon points="40,0 130,0 420,208 420,272" fill="#3b5a78" opacity=".55"/>
        <polygon points="420,272 420,594 130,594" fill="#eef1f8"/>
      </svg>

      <div class="cover-title">
        <h1>BROCHURE</h1>
        <p>ZentaLOOM 2021</p>
      </div>

      <div class="brand-name">ZentaLOOM</div>
    </section>
  </main>
</body>
</html>
```